A start up special flyer design!

Hi All - Have updated the attachment content - This is the info required for the designs.
I need a catchy flyer to send out to a few areas to advertise the start of my plumbing business!
The flyer will contain an offer for customers, which will need to have some key details on it. See attached. Feel free to fit these criteria into the flyer given your knowledge on design and messaging principles. Key thing to get across to customers is the discount and special offer, and that it is a start up offer.
I have a logo that needs to be on the flyer as well - let me know what format you require and I will send through to you.
The color scheme needs to be blue / grey / black / white.
Let me know if you have any questions.
I

```html
<!DOCTYPE html>
<html lang="en">
<head>
<meta charset="utf-8">
<title>Marlow Pipe Plumbing – Start-up Offer Flyer</title>
<link href="https://fonts.googleapis.com/css2?family=Jost:wght@300;400;600;700;800&family=Montserrat:wght@700;800&display=swap" rel="stylesheet">
<style>
  :root {
    --charcoal: #3d3d3f;
    --ink: #333335;
    --white: #ffffff;
    --blue: #1a75bc;
    --blue-soft: rgba(64, 124, 197, 0.92);
    --blue-text: #2a7fc4;
    --page: #efefef;
  }
  * { margin: 0; padding: 0; box-sizing: border-box; }
  html, body {
    width: 1200px; height: 1200px; overflow: hidden;
    background: var(--page);
    font-family: "Jost", sans-serif;
  }
  .flyer {
    position: absolute; left: 40px; top: 168px;
    width: 1120px; height: 864px;
    background: var(--white);
    box-shadow: 0 6px 24px rgba(0,0,0,0.18);
    overflow: hidden;
  }
  .header {
    position: absolute; left: 0; top: 0; width: 100%; height: 152px;
    background: var(--charcoal); color: var(--white);
  }
  .brand {
    position: absolute; left: 52px; top: 36px;
    font-family: "Montserrat", sans-serif; font-weight: 800;
    font-size: 25px; line-height: 28px; letter-spacing: 3.5px;
  }
  .services {
    position: absolute; right: 52px; top: 52px;
    font-weight: 300; font-size: 38px; line-height: 1;
  }
  .hero-photo {
    position: absolute; left: 360px; top: 152px; width: 760px; height: 328px;
    background:
      radial-gradient(ellipse at 85% 40%, #b8302b 0%, rgba(184,48,43,0.85) 18%, rgba(184,48,43,0) 42%),
      radial-gradient(ellipse at 45% 75%, rgba(190,150,90,0.7) 0%, rgba(190,150,90,0) 35%),
      linear-gradient(90deg, #ffffff 0%, #eceef0 28%, #cfcbc6 55%, #b9b2ab 75%, #a8504a 100%);
  }
  .offer-tag {
    position: absolute; left: 54px; top: 210px; width: 218px; height: 58px;
    background: var(--ink); color: var(--white);
    font-family: "Montserrat", sans-serif; font-weight: 800;
    font-size: 46px; line-height: 58px; letter-spacing: 4px; text-align: center;
  }
  .discount {
    position: absolute; left: 50px; top: 262px; color: var(--ink);
  }
  .discount-number {
    position: absolute; left: 0; top: 0;
    font-family: "Montserrat", sans-serif; font-weight: 800;
    font-size: 152px; line-height: 1; letter-spacing: -10px;
  }
  .discount-percent {
    position: absolute; left: 150px; top: 2px;
    font-family: "Montserrat", sans-serif; font-weight: 800;
    font-size: 72px; line-height: 1;
  }
  .discount-off {
    position: absolute; left: 152px; top: 60px;
    font-family: "Montserrat", sans-serif; font-weight: 800;
    font-size: 58px; line-height: 1;
  }
  .discount-note {
    position: absolute; left: 52px; top: 392px;
    font-weight: 300; font-size: 35px; line-height: 1; color: var(--ink);
  }
  .quote-band {
    position: absolute; left: 314px; top: 329px; width: 806px; height: 96px;
    background: var(--blue-soft); color: var(--white);
    font-weight: 300; font-size: 35px; line-height: 96px;
    padding-left: 28px; white-space: nowrap;
  }
  .benefits {
    position: absolute; left: 0; top: 480px; width: 100%; height: 120px;
    background: var(--blue); color: var(--white);
    font-weight: 300; font-size: 38px; line-height: 44px;
    text-align: center; padding-top: 16px;
  }
  .booking {
    position: absolute; left: 0; top: 626px; width: 100%;
    font-weight: 300; font-size: 38px; line-height: 44px;
    color: var(--ink); text-align: center;
  }
  .terms {
    position: absolute; left: 0; top: 758px; width: 100%;
    font-weight: 400; font-size: 13.5px; color: var(--blue-text); text-align: center;
  }
  .footer {
    position: absolute; left: 0; bottom: 0; width: 100%; height: 76px;
    background: var(--charcoal); color: var(--white);
    display: flex; align-items: center; justify-content: center; gap: 10px;
    font-weight: 300; font-size: 18px;
  }
  .contact { display: flex; align-items: center; gap: 7px; }
  .contact svg { width: 26px; height: 26px; }
  .divider { opacity: 0.9; }
</style>
</head>
<body>
  <main class="flyer">
    <header class="header">
      <div class="brand">MARLOW<br>PIPE<br>PLUMBING</div>
      <div class="services">All plumbing, draining, and gasfitting works</div>
    </header>

    <div class="hero-photo" role="img" aria-label="Close-up of a red pipe wrench with brass and copper plumbing fittings on a wet white surface"></div>

    <div class="offer-tag">OFFER</div>
    <div class="discount">
      <span class="discount-number">15</span>
      <span class="discount-percent">%</span>
      <span class="discount-off">off</span>
    </div>
    <div class="discount-note">your overall bill*</div>

    <div class="quote-band">“Quality work at a decent price” | “Local plumber”</div>

    <section class="benefits">
      No GST payable, saving you additional 10% on your bill<br>
      Plus, a free hot water health check and replacement quote
    </section>

    <p class="booking">
      To make an appointment, call or email Dean, or<br>
      alternatively make a booking directly on the website
    </p>

    <p class="terms">*Offer valid between 15 August 2016 to 15 October 2016 • Valid until 30 September 2016 • Quote valid for 12 months from the quote date.</p>

    <footer class="footer">
      <span class="contact">
        <svg viewBox="0 0 26 26" aria-hidden="true"><circle cx="13" cy="13" r="11.5" fill="none" stroke="#fff" stroke-width="1.6"/><path d="M10 7.5c-1.5 1-2 3-1.2 5.5s2.5 4.8 4.6 6c1 .6 1.8.3 2.5-.5l.6-.8-2.3-2-1 .8c-1-.6-2.2-2.4-2.6-3.7l1.1-.6-.9-3z" fill="#fff"/></svg>
        0400 182 640
      </span>
      <span class="divider">|</span>
      <span class="contact">
        <svg viewBox="0 0 26 26" aria-hidden="true"><circle cx="13" cy="13" r="11.5" fill="none" stroke="#fff" stroke-width="1.6"/><circle cx="13" cy="13" r="4" fill="none" stroke="#fff" stroke-width="1.6"/><path d="M17 10v4.5c0 1.5 2.5 1.5 2.5-1" fill="none" stroke="#fff" stroke-width="1.6"/></svg>
        dean@marlowpipeplumbing.com
      </span>
      <span class="divider">|</span>
      <span class="contact">
        <svg viewBox="0 0 26 26" aria-hidden="true"><g fill="none" stroke="#fff" stroke-width="1.4"><circle cx="13" cy="13" r="11"/><ellipse cx="13" cy="13" rx="5" ry="11"/><path d="M2 13h22M4 7.5h18M4 18.5h18M13 2v22"/></g></svg>
        www.marlowpipeplumbing.com
      </span>
    </footer>
  </main>
</body>
</html>
```